Technology, Futuristic Innovation & Artificial Intelligence

I am looking for something with Artificial Intelligence DNA strands....
Blue, black, with white dna strands........I like clean, crisp, professional and not busy look.................................................................................................................................................................................................................................................................................................................................................................................. Thanks!

Target Market(s)

Engineers and United States Government Contractors

Industry/Entity Type

Engineering

Contact Information for Business Card

I've uploaded my logo the certification logo.

Font styles to use
Serif

Colors
3176b5
33a6d7
ffffff

Requirements
Must have
• Name
• Title
• Address
• Phone number
• website name
• certification logo
Nice to have
• Something with Artificial Intelligence DNA strands......
• **Please note it would be nice to have the business card 3D or textured with raised images. Thanks
Should not have
• Please no feminine flowery designs....this is an engineering firm

```html
<!DOCTYPE html>
<html lang="en">
<head>
<meta charset="utf-8">
<title>Corvane Business Card</title>
<link rel="stylesheet" href="https://fonts.googleapis.com/css2?family=Oswald:wght@400&family=Work+Sans:wght@400&display=swap">
<style>
  :root {
    --page: #e9e9ec;
    --navy-deep: #05081c;
    --navy: #14205a;
    --blue: #3176b5;
    --cyan: #33a6d7;
    --white: #ffffff;
    --ink: #1b1b22;
    --swoosh: #0b0f2c;
  }
  * { margin: 0; padding: 0; box-sizing: border-box; }
  html, body { width: 1200px; height: 930px; overflow: hidden; background: var(--page); }
  .canvas { position: relative; width: 1200px; height: 930px; }
  .card {
    position: absolute; left: 278px; width: 645px; height: 368px;
    border-radius: 22px; overflow: hidden; background: var(--navy-deep);
    box-shadow: 0 6px 18px rgba(0,0,0,.25);
  }
  .card--front { top: 76px; }
  .card--back { top: 484px; height: 370px; }
  .circuit-field {
    position: absolute; inset: 0;
    background:
      radial-gradient(ellipse at 70% 30%, rgba(51,166,215,.35), transparent 55%),
      radial-gradient(ellipse at 20% 80%, rgba(49,118,181,.3), transparent 60%),
      linear-gradient(120deg, var(--navy-deep) 0%, var(--navy) 60%, #1d2c72 100%);
  }
  .card-svg { position: absolute; inset: 0; }
  .naics {
    position: absolute; left: 32px; top: 26px;
    font-family: "Oswald", sans-serif; font-size: 23px; line-height: 30px;
    color: var(--white); letter-spacing: -.2px;
  }
  .brand { position: absolute; display: flex; align-items: center; gap: 12px;
    font-family: "Work Sans", sans-serif; font-weight: 400; color: var(--white);
    text-transform: uppercase; letter-spacing: 3px; }
  .brand-mark { background: var(--cyan); }
  .brand--front { left: 32px; top: 176px; font-size: 34px; }
  .brand--front .brand-mark { width: 22px; height: 22px; }
  .brand--back { left: 0; right: 0; top: 164px; justify-content: center; font-size: 58px; }
  .brand--back .brand-mark { width: 34px; height: 34px; }
  .contact {
    position: absolute; right: 28px; top: 190px; text-align: right;
    font-family: "Work Sans", sans-serif; color: var(--ink);
  }
  .contact-name { font-size: 25px; letter-spacing: .5px; line-height: 1.1; }
  .contact-title { font-size: 15px; margin-top: 4px; }
  .contact-address { font-size: 15.5px; line-height: 21px; margin-top: 12px; }
  .contact-lines { list-style: none; margin-top: 6px; font-size: 15.5px; line-height: 20px; }
  .contact-lines li { display: flex; justify-content: flex-end; align-items: center; gap: 10px; }
  .contact-lines svg { width: 10px; height: 10px; }
  .badge { position: absolute; left: 300px; top: 268px; }
</style>
</head>
<body>
<main class="canvas">
  <section class="card card--front">
    <div class="circuit-field" role="img" aria-label="Glowing blue circuit-board pattern with light particles"></div>
    <svg class="card-svg" viewBox="0 0 645 368" aria-hidden="true">
      <line x1="4" y1="48" x2="28" y2="48" stroke="#b8c2d8" stroke-width="1.5"/>
      <path d="M0,258 C140,300 250,262 360,190 C450,132 545,112 645,172 L645,368 L0,368 Z" fill="#ffffff"/>
      <path d="M0,270 C140,312 250,276 355,206 C300,262 160,316 0,286 Z" fill="var(--swoosh)"/>
      <path d="M370,186 C450,136 545,118 645,176 L645,168 C560,112 460,118 370,186 Z" fill="var(--swoosh)"/>
      <path d="M42,318 C160,322 260,292 350,240 C290,290 170,336 42,318 Z" fill="var(--swoosh)"/>
    </svg>
    <div class="naics">NAICS: 5413-10/30/40, 5416-11/14/18, 5419-90<br>5611-10, 5613--12/20/30, 5614-10</div>
    <div class="brand brand--front"><span class="brand-mark"></span>Corvane</div>
    <div class="contact">
      <p class="contact-name">DANA WHITFIELD</p>
      <p class="contact-title">CEO</p>
      <p class="contact-address">118 Larkspur Lane<br>Meridale, SC 29400</p>
      <ul class="contact-lines">
        <li>555.014.2280
          <svg viewBox="0 0 10 10"><path d="M2,1 L4,1 L4.5,3 L3.3,3.8 C3.8,5 5,6.2 6.2,6.7 L7,5.5 L9,6 L9,8 C5,8.5 1.5,5 2,1 Z" fill="#1b1b22"/></svg></li>
        <li>dwhitfield@corvane.org
          <svg viewBox="0 0 10 10"><rect x="1" y="2" width="8" height="6" fill="none" stroke="#1b1b22"/><path d="M1,2 L5,5.5 L9,2" fill="none" stroke="#1b1b22"/></svg></li>
        <li>www.corvane.org
          <svg viewBox="0 0 10 10"><circle cx="5" cy="5" r="4" fill="none" stroke="#1b1b22"/><ellipse cx="5" cy="5" rx="1.8" ry="4" fill="none" stroke="#1b1b22"/><line x1="1" y1="5" x2="9" y2="5" stroke="#1b1b22"/></svg></li>
      </ul>
    </div>
  </section>

  <section class="card card--back">
    <div class="circuit-field" role="img" aria-label="Glowing blue circuit-board pattern with light particles"></div>
    <svg class="card-svg" viewBox="0 0 645 370" aria-hidden="true">
      <line x1="4" y1="48" x2="90" y2="48" stroke="#b8c2d8" stroke-width="1.5"/>
      <line x1="134" y1="236" x2="298" y2="236" stroke="#ffffff" stroke-width="1.5"/>
      <line x1="48" y1="360" x2="200" y2="360" stroke="#b8c2d8" stroke-width="1"/>
    </svg>
    <div class="brand brand--back"><span class="brand-mark"></span>Corvane</div>
    <svg class="badge" width="92" height="76" viewBox="0 0 92 76" role="img" aria-label="Verified vendor certification badge">
      <circle cx="46" cy="36" r="34" fill="#d9b24a"/>
      <circle cx="46" cy="36" r="27" fill="#1f3a8a"/>
    </svg>
  </section>
</main>
</body>
</html>
```